design a construction company business card

Design business card around our logo. Card must have all the typical info: name, title, address, phone, email, business name, etc. Somewhere on the card I would like to see our motto "Built on integrity... Inspired by commitment." Consider adding a splash of bright orange to the card to complement the blues and silvers/grays in the logo. We are open to metallic inks, textures, etc. We would like to see options on both light and dark backgrounds. The font in the logo is Euro Technic Extended Regular.

```html
<!DOCTYPE html>
<html lang="en">
<head>
<meta charset="UTF-8">
<title>Halden Builders – Business Card</title>
<link href="https://fonts.googleapis.com/css2?family=Michroma&family=Roboto:wght@400;500&display=swap" rel="stylesheet">
<style>
  :root {
    --stage: #2a2b2d;
    --card-dark: #0c0c0d;
    --card-dark-edge: #1c1c1e;
    --card-light: #ffffff;
    --brand-blue: #2450a6;
    --brand-blue-deep: #1b3f8c;
    --steel: #8a8d92;
    --steel-light: #c9cbce;
    --ink: #2b2b2b;
    --silver: #b9bbbf;
  }
  * { box-sizing: border-box; margin: 0; padding: 0; }
  html, body { width: 1200px; height: 902px; overflow: hidden; }
  body { background: var(--stage); position: relative; font-family: "Roboto", Arial, sans-serif; }

  .card {
    position: absolute;
    width: 560px;
    height: 320px;
    border-radius: 22px;
    overflow: hidden;
    box-shadow: 0 10px 30px rgba(0,0,0,.45);
  }

  /* Dark front */
  .card-front {
    left: 80px; top: 100px;
    background: linear-gradient(135deg, var(--card-dark-edge) 0%, var(--card-dark) 60%);
  }
  .front-brand {
    position: absolute; left: 0; right: 0; top: 100px;
    text-align: center;
    font-family: "Michroma", sans-serif;
    color: var(--silver);
  }
  .front-brand .brand-main { font-size: 46px; letter-spacing: 4px; line-height: 1; }
  .front-brand .brand-sub { font-size: 13px; letter-spacing: 3px; margin-top: 10px; }
  .motto {
    position: absolute; left: 0; right: 0; bottom: 34px;
    text-align: center;
    font-family: "Michroma", sans-serif;
    font-size: 12px; letter-spacing: 1.5px;
    color: var(--steel);
  }

  /* Light back */
  .card-back {
    left: 560px; top: 480px;
    background: var(--card-light);
  }
  .person { position: absolute; left: 36px; top: 64px; }
  .person-name {
    font-family: "Michroma", sans-serif;
    font-size: 15px; letter-spacing: 1px;
    color: var(--brand-blue);
  }
  .person-title {
    font-family: "Michroma", sans-serif;
    font-size: 11px; letter-spacing: 1px;
    color: var(--steel); margin-top: 6px;
  }
  .back-brand {
    position: absolute; right: 34px; top: 38px;
    width: 220px; text-align: center;
    font-family: "Michroma", sans-serif;
    color: var(--brand-blue);
  }
  .back-brand .brand-main { font-size: 32px; letter-spacing: 3px; line-height: 1; }
  .back-brand .brand-sub { font-size: 10px; letter-spacing: 2px; margin-top: 8px; }
  .rule { position: absolute; height: 1px; background: var(--steel-light); }
  .rule-brand { right: 34px; top: 126px; width: 230px; }
  .rule-contact { left: 36px; top: 230px; width: 330px; }

  .address {
    position: absolute; right: 40px; top: 150px;
    display: flex; gap: 8px; align-items: flex-start;
    font-size: 13px; line-height: 1.45; color: var(--ink);
  }
  .contacts { position: absolute; left: 36px; top: 244px; font-size: 14px; color: var(--ink); }
  .contact-row { display: flex; align-items: center; gap: 10px; height: 24px; }
  .icon { width: 14px; height: 14px; flex: none; }

  .base-strip { position: absolute; left: 0; bottom: 0; width: 100%; height: 14px; background: var(--steel-light); }
  .web-band { position: absolute; right: 0; bottom: 0; width: 260px; height: 60px; }
  .web-text {
    position: absolute; right: 28px; bottom: 20px;
    font-size: 14px; color: #fff; letter-spacing: .3px;
  }
</style>
</head>
<body>

  <section class="card card-front" aria-label="Business card front">
    <div class="front-brand">
      <div class="brand-main">HALDEN</div>
      <div class="brand-sub">BUILDERS, INC.</div>
    </div>
    <p class="motto">GROUNDED IN CRAFT ... DRIVEN BY TRUST</p>
  </section>

  <section class="card card-back" aria-label="Business card back">
    <div class="person">
      <div class="person-name">MARCUS DELANEY</div>
      <div class="person-title">CEO/FOUNDER</div>
    </div>

    <div class="back-brand">
      <div class="brand-main">HALDEN</div>
      <div class="brand-sub">BUILDERS, INC.</div>
    </div>
    <div class="rule rule-brand"></div>

    <div class="address">
      <svg class="icon" viewBox="0 0 14 14" aria-hidden="true">
        <path d="M7 1a4.5 4.5 0 0 0-4.5 4.5C2.5 9 7 13 7 13s4.5-4 4.5-7.5A4.5 4.5 0 0 0 7 1z" fill="none" stroke="var(--brand-blue)" stroke-width="1.6"/>
        <circle cx="7" cy="5.5" r="1.6" fill="var(--brand-blue)"/>
      </svg>
      <div>Ridgeline Commerce Drive<br>Suite 310, Fairview</div>
    </div>

    <div class="rule rule-contact"></div>
    <div class="contacts">
      <div class="contact-row">
        <svg class="icon" viewBox="0 0 14 14" aria-hidden="true">
          <path d="M3 1.5l2 .3 1 3-1.4 1a7 7 0 0 0 3.6 3.6l1-1.4 3 1 .3 2c-.2.8-1 1.3-1.8 1.2C5.4 11.7 2.3 8.6 1.8 3.3 1.7 2.5 2.2 1.7 3 1.5z" fill="var(--brand-blue)"/>
        </svg>
        <span>555.014.2297</span>
      </div>
      <div class="contact-row">
        <svg class="icon" viewBox="0 0 14 14" aria-hidden="true">
          <rect x="1" y="3" width="12" height="8.5" fill="var(--brand-blue)"/>
          <path d="M1 3l6 5 6-5" fill="none" stroke="#fff" stroke-width="1"/>
        </svg>
        <span>marcus@halden.com</span>
      </div>
    </div>

    <div class="base-strip"></div>
    <svg class="web-band" viewBox="0 0 260 60" preserveAspectRatio="none" aria-hidden="true">
      <polygon points="30,0 260,0 260,60 0,60" fill="var(--brand-blue-deep)"/>
    </svg>
    <span class="web-text">www.haldenbuilders.com</span>
  </section>

</body>
</html>
```